Volmira Logo and business card

We need a business card and logo, we are currently using a logo that we like but would like to be a bit more streamlined. We deal with very high end clients and our business card needs to reflect that. We would love to see and hire somebody that can deliver a very MODERN, simple design. With he main front of the card to be black with either a red lettering or White to provide great contrast. I would like to have a minimalist abstract picture of a heavy machine on it but it is not a requirement ( most likely an Crane ( a bold heron crane with a bucket would be perfect or maybe a vendari 270 XT )) If it keeps in line with being a classic simple, and modern design. Letterpress is also an option where it gives it a great look and texture, the card will be printed on a thick stock. On the back there needs to be a star included somewhere on the card and design, this represents the first generation that started the company back in 1936 therefore it is a sentimental addition ( make it modern and simple)
We do not want a cheesy construction template. We do heavy site work, aka we use excavators, payloaders, off road rok j40 trucks, very big fun toys.
There is a huge chance to get the web design as well for the winning design.
Have fun, cannot wait to see the designs!
In addition, we'd like to point out that our primary need and priority is still the BUSINESS CARD design itself. The logo has to complement the overall look of the business card, but it is secondary to the card's look. Please keep this in mind.
Thank you,
Gerald
Target Market(s)
General Contractors, upscale home owners ( house values of 1M plus)
and commercial property owners.
Projects range from $5000 to 1 million.
Industry/Entity Type
Construction
Requirements
Must have
- Star incorporated into design
Nice to have
- an abstract heavy site work machine ( pics attached) If it keeps in line with being a classic simple, and modern design.
I would like to have black and red on the design since all the lettering on the trucks is red, but i will let the designer take care of that.

```html
<!DOCTYPE html>
<html lang="en">
<head>
<meta charset="utf-8">
<title>Volmira Business Card</title>
<link rel="stylesheet" href="https://fonts.googleapis.com/css2?family=Quicksand:wght@400;500;700&display=swap">
<style>
  :root {
    --bg-light: #f4f4f4;
    --bg-dark: #cfcfcf;
    --card-black: #1c1c1e;
    --card-white: #f7f7f7;
    --card-grey: #b9b9b9;
    --brand-red: #d8141b;
    --ink: #1a1a1a;
    --star-light: #e9e9e9;
  }
  html, body {
    margin: 0;
    width: 1200px;
    height: 1200px;
    overflow: hidden;
  }
  body {
    background: radial-gradient(circle at 30% 20%, var(--bg-light), var(--bg-dark));
    font-family: "Quicksand", sans-serif;
  }
  .card {
    position: absolute;
    left: 320px;
    width: 560px;
    height: 320px;
    box-shadow: 0 10px 28px rgba(0,0,0,0.22);
  }
  .card--front { top: 230px; }
  .card--back { top: 630px; }
  .card svg { display: block; width: 100%; height: 100%; }
  .brand-name { font-family: "Quicksand", sans-serif; font-weight: 500; fill: var(--brand-red); }
  .brand-sub { font-family: "Quicksand", sans-serif; font-weight: 500; fill: var(--brand-red); }
  .contact-text { font-family: "Quicksand", sans-serif; font-weight: 500; font-size: 11px; fill: var(--ink); }
  .person-name { font-family: "Quicksand", sans-serif; font-weight: 700; font-size: 17px; fill: var(--ink); letter-spacing: 1px; }
  .person-title { font-family: "Quicksand", sans-serif; font-weight: 500; font-size: 12px; fill: var(--ink); }
</style>
</head>
<body>

  <div class="card card--front">
    <svg viewBox="0 0 560 320" xmlns="http://www.w3.org/2000/svg">
      <defs>
        <linearGradient id="skylineFade" x1="0" y1="0" x2="0" y2="1">
          <stop offset="0" stop-color="#2a2a2c" stop-opacity="0.2"/>
          <stop offset="0.6" stop-color="#333335" stop-opacity="0.9"/>
          <stop offset="1" stop-color="#1c1c1e" stop-opacity="0"/>
        </linearGradient>
      </defs>
      <rect class="front-base" width="560" height="320" fill="var(--card-black)"/>
      <rect class="front-skyline" x="0" y="20" width="560" height="120" fill="url(#skylineFade)"
            role="img" aria-label="Faint silhouette of excavators, cranes and site machinery along the horizon"/>
      <line class="front-rule" x1="0" y1="150" x2="560" y2="150" stroke="var(--brand-red)" stroke-width="1.5"/>
      <text class="brand-name" x="268" y="140" font-size="34">Volmira</text>
      <text class="brand-sub" x="270" y="170" font-size="13">Industries Inc.</text>
    </svg>
  </div>

  <div class="card card--back">
    <svg viewBox="0 0 560 320" xmlns="http://www.w3.org/2000/svg">
      <rect class="back-base" width="560" height="320" fill="var(--card-white)"/>
      <polygon class="back-grey-panel" points="0,190 330,205 420,320 0,320" fill="var(--card-grey)"/>
      <polygon class="back-black-panel" points="235,0 560,0 560,150 330,205" fill="var(--card-black)"/>

      <polygon class="heritage-star" fill="var(--star-light)"
               points="520,22 523.5,32 534,32 525.5,38.5 528.8,48.5 520,42.3 511.2,48.5 514.5,38.5 506,32 516.5,32"/>

      <text class="brand-name" x="340" y="90" font-size="30">Volmira</text>
      <text class="brand-sub" x="342" y="112" font-size="12">Industries Inc.</text>

      <g class="contact-address">
        <text class="contact-text" x="40" y="40">2140 Quarry Ridge Road</text>
        <text class="contact-text" x="40" y="55">Suite 12, Harlow Bay</text>
        <text class="contact-text" x="40" y="70">NJ 07410</text>
      </g>

      <g class="contact-icons" fill="var(--brand-red)">
        <circle cx="28" cy="96" r="6"/>
        <circle cx="28" cy="111" r="6"/>
        <circle cx="28" cy="126" r="6"/>
        <path d="M25.5 93 l1.5 0 l0.8 2 l-1 0.8 q0.8 1.6 2.2 2.2 l0.8 -1 l2 0.8 l0 1.5 q-4 0.5 -6.3 -6.3z" fill="#fff"/>
        <rect x="25" y="108" width="6" height="6" rx="1" fill="none" stroke="#fff" stroke-width="1"/>
        <path d="M24.5 123.5 h7 v5 h-7z M24.5 123.5 l3.5 2.5 l3.5 -2.5" fill="none" stroke="#fff" stroke-width="1"/>
      </g>
      <g class="contact-lines">
        <text class="contact-text" x="40" y="100">+1 201 555 0148</text>
        <text class="contact-text" x="40" y="115">+1 (201) 555 0192</text>
        <text class="contact-text" x="40" y="130">office@volmira.com</text>
      </g>

      <text class="person-name" x="345" y="250">Gerald Marek</text>
      <text class="person-title" x="345" y="270">Site Work Project Lead</text>
    </svg>
  </div>

</body>
</html>
```